Construction Business Card Design

We have a landscape construction company based in Australia
Were out of business cards ,
So now we're after a fresh looking modern card to give a fresh look to our business ....
We would like the business card to have the
(Front)
Tallow Ridge Pty Ltd
Director Norman Cusk
0462395108
(Back)
Landscape,Construction,Paving,Excavation
(In smaller font low in the frame of card)
Different textures , curved edge , vertical and horizontal designs also minimal colours per design
Eg one side black , one coloured or a splash here or there
Industry/Entity Type
Landscape
Contact Information for Business Card
Tallow Ridge Pty Ltd
Director Norman Cusk
0462395108
Landscape,Paving,Construction,Excavation
Look and feel

```html
<!DOCTYPE html>
<html lang="en">
<head>
<meta charset="UTF-8">
<title>Tallow Ridge Pty Ltd – Business Card</title>
<link rel="stylesheet" href="https://fonts.googleapis.com/css2?family=Questrial&family=Poppins:wght@600&display=swap">
<style>
  :root {
    --paper: #ffffff;
    --accent: #f68b1f;
    --charcoal: #272727;
    --white: #ffffff;
  }
  html, body {
    margin: 0;
    padding: 0;
    width: 741px;
    height: 1200px;
    overflow: hidden;
    background: var(--paper);
  }
  .card {
    position: relative;
    width: 741px;
    height: 1200px;
    background: var(--paper);
    overflow: hidden;
  }
  .accent-side {
    position: absolute;
    left: 0;
    top: 0;
    width: 36px;
    height: 1200px;
    background: var(--accent);
  }
  .accent-base {
    position: absolute;
    left: 0;
    bottom: 0;
    width: 741px;
    height: 34px;
    background: var(--accent);
  }
  .panel {
    position: absolute;
    left: 36px;
    top: 0;
    width: 705px;
    height: 1166px;
    background: var(--charcoal);
    border-top-right-radius: 135px;
  }
  .details {
    position: absolute;
    left: 81px;
    top: 950px;
    font-family: "Questrial", "Century Gothic", sans-serif;
  }
  .company {
    margin: 0 0 30px;
    white-space: nowrap;
    line-height: 1;
    font-weight: 400;
  }
  .company-name {
    font-family: "Poppins", "Century Gothic", sans-serif;
    font-weight: 600;
    font-size: 44px;
    color: var(--white);
    letter-spacing: 0.2px;
  }
  .company-suffix {
    font-family: "Questrial", "Century Gothic", sans-serif;
    font-weight: 400;
    font-size: 30px;
    color: var(--accent);
    margin-left: 10px;
  }
  .contact {
    margin: 0;
    padding: 0;
    list-style: none;
    color: var(--accent);
    font-size: 32px;
    line-height: 35px;
  }
</style>
</head>
<body>
  <div class="card">
    <div class="accent-side"></div>
    <div class="accent-base"></div>
    <div class="panel"></div>
    <div class="details">
      <h1 class="company"><span class="company-name">Tallow Ridge</span><span class="company-suffix">Pty Ltd</span></h1>
      <ul class="contact">
        <li class="contact-role">Director Norman Cusk</li>
        <li class="contact-email">Tallowridgeptyltd@gmail.com</li>
        <li class="contact-phone">0462395108</li>
      </ul>
    </div>
  </div>
</body>
</html>
```